Website for cardiology consultation and diagnostics in Canada

Hi there, thank you for considering to take on this project.

Our Cardiology would like designs for a website. we are a cardiology group comprised of 7 doctors. We need a functioning site.

Key design themes should highlight simplicity and serenity. Website shouldnt be complicated or crowded. Less words and more graphics. It should be mobile friendly. The winning submission should work with us for revisions until we get it right.

Sections:
Front page - who we are, why choose us. (1 - 2 paragraphs, Lorem Ipsum)

1. Requisition form (can download our latest requisition form, and create the same form online for submission as well)
2. Services provided: EKG, Echo, Stress Echo, Holter, Loop, Ambulatory BP monitors. One or two paragraphs on each of these tests with graphics.
3. Our physicians: Dr A, B, C, D, E, F, G (short bio with random pix)
4. About us: A few paragraph about how we started (Lorem Ipsum)
5. Location : design a simple page for our Address and location (map)
6. Contact us : design a page for feedback

We have included most of the material in other aspects of our practice including our color themes and logos

Current website is larkfieldpulse.org

Target Market(s)

Other physicians, patients

Industry/Entity Type

Health Care

Number of Pages Required

5+ page

Requirements
Must have
• Pages as described above
• Ability to do revisions later
• Pictures
• Simple and elegant
Should not have
• Too wordy or complicated designs

```html
<!DOCTYPE html>
<html lang="en">
<head>
<meta charset="utf-8">
<title>Physicians – Larkfield Pulse Institute</title>
<link rel="stylesheet" href="https://fonts.googleapis.com/css2?family=Roboto:wght@300;400;500&display=swap">
<style>
:root{
  --navy:#2e2a5e;
  --red:#c8262f;
  --blue:#0a7fc9;
  --text:#4a4a4a;
  --muted:#666;
  --line:#e4e4e4;
  --footer:#f4f4f4;
  --white:#fff;
}
*{margin:0;padding:0;box-sizing:border-box}
html,body{width:1170px;height:1200px;overflow:hidden;background:var(--white);font-family:'Roboto',Arial,sans-serif;color:var(--text)}
.page{position:relative;width:1170px;height:1200px}

.main-nav{height:55px;background:var(--navy);display:flex;justify-content:center;align-items:center;gap:0}
.main-nav a{color:var(--white);text-decoration:none;font-size:13px;font-weight:500;padding:0 26px;position:relative;line-height:55px}
.main-nav a.active::after{content:"";position:absolute;left:50%;bottom:11px;width:34px;height:2px;background:var(--red);transform:translateX(-50%)}

.top-bar{height:120px;display:flex;align-items:center;justify-content:space-between;padding:0 0 0 183px;position:relative}
.contact-item{display:flex;align-items:center;gap:7px;font-size:14px;color:#333}
.contact-item svg{flex:none}
.contact-email{position:absolute;right:163px;top:50%;transform:translateY(-50%)}
.brand{position:absolute;left:50%;top:50%;transform:translate(-50%,-50%);display:flex;flex-direction:column;align-items:center;gap:6px}
.brand-dot{width:22px;height:22px;border-radius:50%;background:var(--red)}
.brand-name{font-size:14px;font-weight:500;color:var(--navy);text-align:center;line-height:1.2;letter-spacing:.5px}

.page-title{margin-top:56px;text-align:center;font-size:37px;font-weight:400;color:var(--red);letter-spacing:.5px}

.physician-grid{margin:53px 0 0 137px;display:grid;grid-template-columns:repeat(3,304px);row-gap:70px}
.physician-card{width:290px}
.card-head{display:flex;align-items:flex-start;gap:10px}
.portrait{width:130px;height:117px;border:1px solid var(--line);background:linear-gradient(180deg,#f6f6f6 0%,#e9edf2 60%,#dfe6ee 100%);flex:none}
.card-name{margin-top:38px}
.card-name h2{font-size:14px;font-weight:400;color:var(--red)}
.card-name p{font-size:11px;color:var(--muted);margin-top:5px}
.card-bio{font-size:14px;font-weight:300;line-height:23.5px;color:var(--text);margin-top:12px;width:270px}
.view-profile{display:inline-block;margin:15px 0 0 2px;background:var(--blue);color:var(--white);font-size:11px;font-weight:500;text-decoration:none;height:27px;line-height:27px;padding:0 10px}

.site-footer{position:absolute;left:0;right:0;bottom:0;height:245px;background:var(--footer);text-align:center}
.site-footer .brand{position:static;transform:none;margin-top:48px;display:inline-flex}
.footer-nav{margin-top:30px;font-size:14px;color:#333;display:flex;justify-content:center;gap:0}
.footer-nav a{color:#333;text-decoration:none}
.footer-nav span{padding:0 17px}
.copyright{margin-top:26px;font-size:14px;color:#333}
</style>
</head>
<body>
<div class="page">
  <nav class="main-nav">
    <a href="#">HOME</a>
    <a href="#">ABOUT US</a>
    <a href="#">SERVICES</a>
    <a href="#">REQUISITION FORM</a>
    <a href="#" class="active">PHYSICIANS</a>
    <a href="#">LOCATION</a>
    <a href="#">CONTACT US</a>
  </nav>

  <header class="top-bar">
    <div class="contact-item">
      <svg width="12" height="12" viewBox="0 0 24 24"><path fill="#c8262f" d="M6.6 10.8a15.1 15.1 0 0 0 6.6 6.6l2.2-2.2a1 1 0 0 1 1-.25 11.4 11.4 0 0 0 3.6.57 1 1 0 0 1 1 1V20a1 1 0 0 1-1 1A17 17 0 0 1 3 4a1 1 0 0 1 1-1h3.5a1 1 0 0 1 1 1c0 1.25.2 2.45.57 3.57a1 1 0 0 1-.25 1z"/></svg>
      519-555-0182
    </div>
    <div class="brand">
      <div class="brand-dot"></div>
      <div class="brand-name">LARKFIELD PULSE<br>INSTITUTE</div>
    </div>
    <div class="contact-item contact-email">
      <svg width="15" height="12" viewBox="0 0 20 16"><rect x="1" y="1" width="18" height="14" rx="1.5" fill="none" stroke="#c8262f" stroke-width="2"/><path d="M1.5 2l8.5 7 8.5-7" fill="none" stroke="#c8262f" stroke-width="2"/></svg>
      CONTACT@LARKFIELDPULSE.ORG
    </div>
  </header>

  <h1 class="page-title">PHYSICIANS</h1>

  <section class="physician-grid">
    <article class="physician-card">
      <div class="card-head">
        <div class="portrait" role="img" aria-label="Portrait photo of a smiling male cardiologist in a white coat"></div>
        <div class="card-name"><h2>DR.ALAN BREWER</h2><p>Cardiologist</p></div>
      </div>
      <p class="card-bio">Sed ut perspiciatis unde omnis iste natus error sit voluptatem accusantium doloremque laudantium</p>
      <a href="#" class="view-profile">VIEW PROFILE</a>
    </article>
    <article class="physician-card">
      <div class="card-head">
        <div class="portrait" role="img" aria-label="Portrait photo of a female doctor with a stethoscope"></div>
        <div class="card-name"><h2>DR.ALAN BREWER</h2><p>Cardiologist</p></div>
      </div>
      <p class="card-bio">Sed ut perspiciatis unde omnis iste natus error sit voluptatem accusantium doloremque laudantium</p>
      <a href="#" class="view-profile">VIEW PROFILE</a>
    </article>
    <article class="physician-card">
      <div class="card-head">
        <div class="portrait" role="img" aria-label="Portrait photo of a male doctor in a white coat and tie"></div>
        <div class="card-name"><h2>DR.ALAN BREWER</h2><p>Cardiologist</p></div>
      </div>
      <p class="card-bio">Sed ut perspiciatis unde omnis iste natus error sit voluptatem accusantium doloremque laudantium</p>
      <a href="#" class="view-profile">VIEW PROFILE</a>
    </article>
    <article class="physician-card">
      <div class="card-head">
        <div class="portrait" role="img" aria-label="Portrait photo of a senior male physician in a white coat"></div>
        <div class="card-name"><h2>DR.ALAN BREWER</h2><p>Cardiologist</p></div>
      </div>
      <p class="card-bio">Sed ut perspiciatis unde omnis iste natus error sit voluptatem accusantium doloremque laudantium</p>
      <a href="#" class="view-profile">VIEW PROFILE</a>
    </article>
    <article class="physician-card">
      <div class="card-head">
        <div class="portrait" role="img" aria-label="Portrait photo of a young male doctor with a stethoscope"></div>
        <div class="card-name"><h2>DR.ALAN BREWER</h2><p>Cardiologist</p></div>
      </div>
      <p class="card-bio">Sed ut perspiciatis unde omnis iste natus error sit voluptatem accusantium doloremque laudantium</p>
      <a href="#" class="view-profile">VIEW PROFILE</a>
    </article>
    <article class="physician-card">
      <div class="card-head">
        <div class="portrait" role="img" aria-label="Portrait photo of a smiling female doctor with curly hair"></div>
        <div class="card-name"><h2>DR.ALAN BREWER</h2><p>Cardiologist</p></div>
      </div>
      <p class="card-bio">Sed ut perspiciatis unde omnis iste natus error sit voluptatem accusantium doloremque laudantium</p>
      <a href="#" class="view-profile">VIEW PROFILE</a>
    </article>
  </section>

  <footer class="site-footer">
    <div class="brand">
      <div class="brand-dot"></div>
      <div class="brand-name">LARKFIELD PULSE<br>INSTITUTE</div>
    </div>
    <nav class="footer-nav">
      <a href="#">HOME</a><span>|</span>
      <a href="#">ABOUT US</a><span>|</span>
      <a href="#">SERVICES</a><span>|</span>
      <a href="#">REQUISITION FORM</a><span>|</span>
      <a href="#">PHYSICIANS</a><span>|</span>
      <a href="#">LOCATION</a><span>|</span>
      <a href="#">CONTACT US</a>
    </nav>
    <p class="copyright">© 2017 COMPANY NAME &nbsp;|&nbsp; ALL RIGHTS RESERVED</p>
  </footer>
</div>
</body>
</html>
```